Etiketten für Bio Seifen
Zielgruppe
Wir stellen hochwertig 'handgemachte' Bio-Seifen her. Die Zielgruppe ist von 3-99 Jahren und zusätzlich haben wir auch noch Seife für Hunde.
Der Firmenname ist 'Kestrima'
Aufgabenstellung
Das Etikett soll Bezug auf Natur, Bio, Nachhaltigkeit nehmen. Wir stellen uns 'weiche' Aquarellfarben vor...Seife: Lavendel, Calendular, 7 Kräuter etc.
Das Etikett soll auf eine Beutelschachtel. Die Schachtel hat eine Anmaße: Breite 55mm; Höhe 120mm; Tiefe 30mm
Das Etikett soll im vorderen- und hinteren Bereich zusammenhängend geklebt werden.
Das Etikett soll eine Abmaße von: Breite 51mm; Höhe 114mm haben (Vorderseite) Rückseite gleich.
Wir möchten die Produkte auch gerne nummerieren, d.h. jede Seife hat eine Nummer die nicht zu groß dargestellt werden soll aber trotzdem gut leserlich.
Wir haben noch ein paar Bilder hochgeladen wie wir uns das ungefähr vorstellen.

```html
<!DOCTYPE html>
<html lang="de">
<head>
<meta charset="utf-8">
<title>Kestrima – Etiketten Bioseife</title>
<link href="https://fonts.googleapis.com/css2?family=Montserrat:wght@400;500&family=Playfair+Display:ital,wght@0,400;1,400;1,700&family=Sacramento&display=swap" rel="stylesheet">
<style>
  :root{
    --navy:#0b3f75;
    --white:#ffffff;
    --trim:#cfcfcf;
    --lav-deep:#6e4fa0;
    --lav-mid:#9b86c4;
    --lav-light:#e4dcef;
    --cal-deep:#eea238;
    --cal-mid:#f6c765;
    --cal-light:#fbe6bb;
    --herb-deep:#2f8d50;
    --herb-mid:#6bb882;
    --herb-light:#dcefe0;
  }
  *{box-sizing:border-box;margin:0;padding:0}
  html,body{width:1200px;height:813px;overflow:hidden;background:var(--white)}
  .sheet{position:relative;width:1200px;height:813px}
  .label{position:absolute;top:47px;width:337px;height:736px;border:1px solid var(--trim)}
  .label--lavender{left:23px}
  .label--calendula{left:433px}
  .label--herbs{left:843px}

  .panel{position:absolute;left:14px;top:0;width:307px;height:705px}
  .artwork{position:absolute;inset:0}
  .label--lavender .artwork{background:
      radial-gradient(ellipse at 20% 25%,var(--lav-deep) 0%,transparent 60%),
      radial-gradient(ellipse at 15% 75%,var(--lav-deep) 0%,transparent 55%),
      linear-gradient(160deg,var(--lav-mid) 0%,var(--lav-light) 70%,var(--lav-mid) 100%)}
  .label--calendula .artwork{background:
      radial-gradient(ellipse at 30% 45%,var(--cal-deep) 0%,transparent 55%),
      radial-gradient(ellipse at 80% 70%,var(--cal-mid) 0%,transparent 60%),
      linear-gradient(170deg,var(--cal-mid) 0%,var(--cal-light) 55%,var(--cal-mid) 100%)}
  .label--herbs .artwork{background:
      radial-gradient(ellipse at 20% 30%,var(--herb-deep) 0%,transparent 60%),
      radial-gradient(ellipse at 25% 80%,var(--herb-deep) 0%,transparent 50%),
      linear-gradient(165deg,var(--herb-mid) 0%,var(--herb-light) 70%,var(--herb-mid) 100%)}

  .brand-card{position:absolute;left:31px;top:30px;width:246px;height:246px;background:var(--white)}
  .brand-frame{position:absolute;left:10px;top:10px;width:226px;height:188px}
  .brand-name{position:absolute;left:0;top:64px;width:246px;text-align:center;
    font:400 46px/1 'Playfair Display',serif;color:var(--navy);letter-spacing:1px}
  .brand-tagline{position:absolute;left:0;top:147px;width:246px;text-align:center;
    font:italic 400 17px/1 'Playfair Display',serif;color:var(--navy)}
  .brand-band{position:absolute;left:10px;top:207px;width:226px;height:29px;background:var(--navy);
    color:var(--white);font:400 13.5px/29px 'Montserrat',sans-serif;text-align:center;letter-spacing:.4px}

  .fold-line{position:absolute;left:0;top:305px;width:307px;border-top:1px dashed rgba(255,255,255,.85)}

  .leaf-mark{position:absolute;left:136px;top:518px;width:38px;height:36px}

  .variant-box{position:absolute;left:41px;top:553px;width:227px;height:78px}
  .variant-box svg{position:absolute;inset:0;width:100%;height:100%}
  .variant-number{position:absolute;left:0;top:15px;width:100%;text-align:center;
    font:400 16px/1 'Montserrat',sans-serif;color:var(--navy)}
  .variant-name{position:absolute;left:0;top:38px;width:100%;text-align:center;
    font:italic 700 21px/1 'Playfair Display',serif;color:var(--navy);letter-spacing:1.5px}

  .benefit-band{position:absolute;left:0;top:656px;width:307px;height:49px;background:var(--navy);
    color:var(--white);text-align:center;font:400 27px/49px 'Sacramento',cursive;white-space:nowrap}
</style>
</head>
<body>
<main class="sheet">

  <section class="label label--lavender">
    <div class="panel">
      <div class="artwork" role="img" aria-label="Aquarellhintergrund in Violett- und Lavendeltönen"></div>
      <div class="brand-card">
        <svg class="brand-frame" viewBox="0 0 226 188" fill="none" stroke="var(--navy)" stroke-width="1.5">
          <polyline points="80,1 225,1 225,65"/>
          <polyline points="225,122 225,187 1,187 1,122"/>
        </svg>
        <div class="brand-name">Kestrima</div>
        <div class="brand-tagline">Natur auf der Haut</div>
        <div class="brand-band">HANDGEMACHTE BIOSEIFE</div>
      </div>
      <div class="fold-line"></div>
      <svg class="leaf-mark" viewBox="0 0 38 36" fill="var(--navy)" aria-hidden="true">
        <path d="M2,0 C18,6 24,20 20,36 C6,32 -2,18 2,0 Z"/>
        <path d="M36,14 C38,24 32,33 22,36 C22,26 27,18 36,14 Z"/>
      </svg>
      <div class="variant-box">
        <svg viewBox="0 0 227 78" fill="var(--white)" stroke="var(--navy)">
          <path d="M6,1 H221 L226,6 V72 L221,77 H6 L1,72 V6 Z" stroke-width="2"/>
          <path d="M9,5 H218 L222,9 V69 L218,73 H9 L5,69 V9 Z" fill="none" stroke-width="1"/>
        </svg>
        <div class="variant-number">N°1</div>
        <div class="variant-name">LAVENDEL</div>
      </div>
      <div class="benefit-band">beruhigend &amp; entspannend</div>
    </div>
  </section>

  <section class="label label--calendula">
    <div class="panel">
      <div class="artwork" role="img" aria-label="Aquarellhintergrund in Gelb- und Orangetönen"></div>
      <div class="brand-card">
        <svg class="brand-frame" viewBox="0 0 226 188" fill="none" stroke="var(--navy)" stroke-width="1.5">
          <polyline points="80,1 225,1 225,65"/>
          <polyline points="225,122 225,187 1,187 1,122"/>
        </svg>
        <div class="brand-name">Kestrima</div>
        <div class="brand-tagline">Natur auf der Haut</div>
        <div class="brand-band">HANDGEMACHTE BIOSEIFE</div>
      </div>
      <div class="fold-line"></div>
      <svg class="leaf-mark" viewBox="0 0 38 36" fill="var(--navy)" aria-hidden="true">
        <path d="M2,0 C18,6 24,20 20,36 C6,32 -2,18 2,0 Z"/>
        <path d="M36,14 C38,24 32,33 22,36 C22,26 27,18 36,14 Z"/>
      </svg>
      <div class="variant-box">
        <svg viewBox="0 0 227 78" fill="var(--white)" stroke="var(--navy)">
          <path d="M6,1 H221 L226,6 V72 L221,77 H6 L1,72 V6 Z" stroke-width="2"/>
          <path d="M9,5 H218 L222,9 V69 L218,73 H9 L5,69 V9 Z" fill="none" stroke-width="1"/>
        </svg>
        <div class="variant-number">N°2</div>
        <div class="variant-name">CALENDULA</div>
      </div>
      <div class="benefit-band">mild reinigend &amp; sanft pflegend</div>
    </div>
  </section>

  <section class="label label--herbs">
    <div class="panel">
      <div class="artwork" role="img" aria-label="Aquarellhintergrund in Grüntönen"></div>
      <div class="brand-card">
        <svg class="brand-frame" viewBox="0 0 226 188" fill="none" stroke="var(--navy)" stroke-width="1.5">
          <polyline points="80,1 225,1 225,65"/>
          <polyline points="225,122 225,187 1,187 1,122"/>
        </svg>
        <div class="brand-name">Kestrima</div>
        <div class="brand-tagline">Natur auf der Haut</div>
        <div class="brand-band">HANDGEMACHTE BIOSEIFE</div>
      </div>
      <div class="fold-line"></div>
      <svg class="leaf-mark" viewBox="0 0 38 36" fill="var(--navy)" aria-hidden="true">
        <path d="M2,0 C18,6 24,20 20,36 C6,32 -2,18 2,0 Z"/>
        <path d="M36,14 C38,24 32,33 22,36 C22,26 27,18 36,14 Z"/>
      </svg>
      <div class="variant-box">
        <svg viewBox="0 0 227 78" fill="var(--white)" stroke="var(--navy)">
          <path d="M6,1 H221 L226,6 V72 L221,77 H6 L1,72 V6 Z" stroke-width="2"/>
          <path d="M9,5 H218 L222,9 V69 L218,73 H9 L5,69 V9 Z" fill="none" stroke-width="1"/>
        </svg>
        <div class="variant-number">N°3</div>
        <div class="variant-name">7 KRÄUTER</div>
      </div>
      <div class="benefit-band">nährend &amp; beruhigend</div>
    </div>
  </section>

</main>
</body>
</html>
```